Mixed Martial Arts Gym Needs a general info flyer

8.5x11
2 sided
Colors: Compliment our logo (attached) Dark Gray, Light Gray, White, Black, Red.
I would like the front of the general info flyer to talk about our general information, listing the offerings bulleted below as well as our address, phone # website etc.
I would also like to highlight that we have relocated to Choctaw, OK as well as mention the owner, head instructor Dale Vorhen: PCL Featherweight veteran, Tulsa Ridge Patrol Officer and Prairie Grappling standout.
We would like a general flyer that talks about our general offerings along with a few pictures. We are a mixed martial arts gym we have moved to a new location in Choctaw, OK. You can find a lot of info on our gym at our website www.k7fightworks.example I've attached pictures as well as an example of a few flyers I like.

This info should be included on front of flyer:
• Adult MMA
• Boxing
• Strength & Conditioning
• Brazilian Jiu Jitsu
• No-Gi Jiu-Jitsu
• Women’s Cardio Kickboxing

• Youth Program: Ages 7-14
Teaching disciplines in Jiu-Jitsu, Judo,
Wrestling, Self-defense

*see our website for rates and our current schedule

We also offer a full fitness facility - Iron Bloom Fitness - with free weights, cardio & cable machines, personal training and fitness classes.
Discounts for Military, Law Enforcement, Fire and College Students.

ON THE BACK OF FLYER:
I would like to include a brief description of each of our classes and an about us. You can find all of that info on our website www.k7fightworks.example as well as pictures.

```html
<!DOCTYPE html>
<html lang="en">
<head>
<meta charset="utf-8">
<title>K7 Fightworks – General Info Flyer</title>
<link rel="stylesheet" href="https://fonts.googleapis.com/css2?family=Archivo+Black&family=Bebas+Neue&family=Michroma&family=Open+Sans:wght@600;700&display=swap">
<style>
  :root {
    --red: #c4201f;
    --red-deep: #8f1513;
    --black: #0d0d0d;
    --dark-gray: #2b2b2b;
    --light-gray: #d9d9d9;
    --white: #ffffff;
    --ink: #1a1a1a;
  }
  * { margin: 0; padding: 0; box-sizing: border-box; }
  html, body { width: 951px; height: 1200px; overflow: hidden; background: var(--white); }
  .flyer { position: relative; width: 951px; height: 1200px; background: var(--white); overflow: hidden; font-family: "Open Sans", sans-serif; }

  .top-rule { position: absolute; left: 0; top: 0; width: 951px; height: 10px; background: var(--red); }
  .header-rule { position: absolute; left: 0; top: 100px; width: 951px; height: 9px; background: var(--red); }

  .hero-photo {
    position: absolute; left: 0; top: 112px; width: 951px; height: 440px;
    background: radial-gradient(ellipse at 35% 45%, #b52a22 0%, #7a1510 45%, #2a0504 100%);
  }
  .hero-rule { position: absolute; left: 0; top: 554px; width: 951px; height: 11px; background: var(--red); }
  .hero-rule::after { content: ""; position: absolute; left: 0; top: 11px; width: 951px; height: 3px; background: var(--black); }

  .gi-photo {
    position: absolute; left: 520px; top: 22px; width: 431px; height: 600px;
    background: linear-gradient(160deg, #f1f1f1 0%, #cfcfcf 40%, #7c6a60 75%, #3a2e2a 100%);
    clip-path: polygon(22% 0, 100% 0, 100% 100%, 31% 100%, 14% 78%, 0 35%);
  }

  .logo-pennant { position: absolute; left: 30px; top: 22px; width: 258px; height: 218px; }
  .logo-name {
    position: absolute; left: 54px; top: 42px; width: 210px; height: 128px;
    background: var(--white); display: flex; align-items: center; justify-content: center; text-align: center;
    font-family: "Archivo Black", sans-serif; font-size: 24px; line-height: 1.15; color: var(--black);
  }

  .fitness-note {
    position: absolute; left: 27px; top: 436px; width: 530px;
    font-family: "Michroma", sans-serif; font-size: 17px; line-height: 1.32; color: var(--white);
  }

  .discounts {
    position: absolute; left: 27px; top: 592px; width: 700px;
    font-family: "Archivo Black", sans-serif; font-size: 36px; line-height: 1.17; color: var(--black); text-transform: uppercase; white-space: nowrap;
  }
  .discounts .accent { color: var(--red); }

  .youth-banner { position: absolute; left: 0; top: 734px; width: 714px; height: 80px; }
  .youth-title {
    position: absolute; left: 28px; top: 740px; white-space: nowrap;
    font-family: "Bebas Neue", sans-serif; font-size: 72px; line-height: 1; color: var(--white);
  }
  .disciplines-bar { position: absolute; left: 0; top: 818px; width: 925px; height: 68px; }
  .disciplines {
    position: absolute; left: 28px; top: 834px;
    font-weight: 700; font-size: 25px; color: var(--white); letter-spacing: -0.2px;
  }

  .corner-shape { position: absolute; left: 0; top: 880px; width: 951px; height: 320px; }

  .offerings { position: absolute; left: 287px; top: 916px; display: flex; gap: 26px; }
  .offerings ul { list-style: none; }
  .offerings li {
    position: relative; padding-left: 26px;
    font-weight: 600; font-size: 22.5px; line-height: 33px; color: var(--dark-gray);
  }
  .offerings li::before {
    content: ""; position: absolute; left: 0; top: 11px; width: 11px; height: 11px; background: var(--red);
  }
  .offerings li.continued::before { display: none; }

  .sparring-photo {
    position: absolute; left: 0; top: 872px; width: 440px; height: 328px;
    background: linear-gradient(135deg, #b8a394 0%, #3d4a8a 35%, #1d1d1d 60%, #e9e9e9 85%, #a08a7c 100%);
    clip-path: polygon(0 0, 212px 0, 262px 178px, 440px 262px, 440px 100%, 0 100%);
  }

  .website {
    position: absolute; left: 507px; top: 1126px; display: flex; align-items: center; gap: 12px;
    font-weight: 700; font-size: 25px; color: var(--white);
  }
  .website svg { width: 26px; height: 26px; }
</style>
</head>
<body>
<div class="flyer">
  <div class="top-rule"></div>
  <div class="header-rule"></div>

  <div class="hero-photo" role="img" aria-label="Photo of two MMA fighters exchanging punches, toned in red"></div>
  <div class="hero-rule"></div>

  <div class="gi-photo" role="img" aria-label="Photo of two Jiu-Jitsu athletes in white gis grappling on the mat"></div>

  <svg class="logo-pennant" viewBox="0 0 258 218" aria-hidden="true">
    <polygon points="0,0 258,0 258,168 129,218 0,168" fill="var(--red)"/>
  </svg>
  <div class="logo-name">K7<br>FIGHTWORKS</div>

  <p class="fitness-note">We also offer a full fitness facility - Iron Bloom Fitness - with free weights, cardio &amp; cable machines, personal training and fitness classes.</p>

  <h2 class="discounts"><span class="accent">Discounts for</span> Military,<br>Law Enforcement, Fire and<br>College Students.</h2>

  <svg class="youth-banner" viewBox="0 0 714 80" aria-hidden="true">
    <polygon points="0,0 674,0 714,80 0,80" fill="var(--red)"/>
  </svg>
  <h2 class="youth-title">Youth Program: Ages 7-14</h2>

  <svg class="disciplines-bar" viewBox="0 0 925 68" aria-hidden="true">
    <polygon points="0,0 925,0 890,68 0,68" fill="var(--black)"/>
  </svg>
  <p class="disciplines">Teaching disciplines in Jiu-Jitsu, Judo, Wrestling, Self-defense</p>

  <svg class="corner-shape" viewBox="0 0 951 320" aria-hidden="true">
    <polygon points="951,22 951,320 0,320 0,253 700,253" fill="var(--black)"/>
    <polyline points="951,4 692,240 0,240" fill="none" stroke="var(--red)" stroke-width="6"/>
  </svg>

  <div class="sparring-photo" role="img" aria-label="Photo of two fighters grappling in no-gi training gear"></div>

  <div class="offerings">
    <ul>
      <li>Brazilian Jiu Jitsu</li>
      <li>No-Gi Jiu-Jitsu</li>
      <li>Women’s Cardio</li>
      <li class="continued">Kickboxing</li>
    </ul>
    <ul>
      <li>Adult MMA</li>
      <li>Boxing</li>
      <li>Strength</li>
      <li class="continued">&amp; Conditioning</li>
    </ul>
  </div>

  <div class="website">
    <svg viewBox="0 0 24 24" fill="none" stroke="currentColor" stroke-width="1.6" aria-hidden="true">
      <circle cx="12" cy="12" r="10"/>
      <ellipse cx="12" cy="12" rx="4.5" ry="10"/>
      <line x1="2" y1="12" x2="22" y2="12"/>
      <path d="M4 6.5h16M4 17.5h16"/>
    </svg>
    <span>www.k7fightworks.example</span>
  </div>
</div>
</body>
</html>
```